Launching a new real estate agency in Monaco

Hello, I am opening a new real estate agency in Monaco. For the purpose of my activity, in order to be known quickly among a fierce competition I need an advertising campaign that will be broadcast in local magazines, newspapers, paper board, etc.

You will find example of pictures of Monaco on which I have the rights and my logo. You can always pick other images that I can buy if the price is reasonable for a commercial use (<200 $)

Please respect the color code.

I wish you good luck and look forward to give you my feedbacks

Reason: Only few projects posted were respecting the brief and of quality. Hoping to receive more in coming days

Target Market(s)

International high-end clientele of all ages, all genders.

Industry/Entity Type

Real Estate Agent

Font styles to use
Serif

Requirements
Must have
• 1/ My logo
• 2/ This message "Un nouveau regard sur l'immobilier" means in English a fresh look at real estate or new eyes on real-estate.
• 3/ My address: 14 rue des Orvilles, Passage Marcellin, 98 000 Monaco
• 4/ Phone number: +377.93.48.25.71
• 5/ Website: www.brunor-agency.com.
• 6/ Format: Files should be easily adjustable but I'd like a vertical display to fit easily in Magazines, Poster and billboard. So please work in high resolution !
Nice to have
• Please think about your design in accordance with the message I want to display.
Should not have
• A simple poster with a picture of Monaco that does not take into consideration the message of the advertisement, "Un nouveau regard sur l'immobilier" which means in english, new eyes on real-estate or a new look at real-estate, or new vision at real-estate.

```html
<!DOCTYPE html>
<html lang="fr">
<head>
<meta charset="utf-8">
<title>Brunor Agency – Un nouveau regard sur l'immobilier</title>
<link rel="stylesheet" href="https://fonts.googleapis.com/css2?family=Abril+Fatface&family=Arimo:wght@400;700&display=swap">
<style>
  :root {
    --page-bg: #e4e4e4;
    --navy: #2b3d58;
    --salmon: #e8ad98;
    --rule: #f4f1ee;
    --lens-edge: #0d0d10;
  }
  * { margin: 0; padding: 0; box-sizing: border-box; }
  html, body {
    width: 1200px; height: 1200px; overflow: hidden;
    background: var(--page-bg);
  }
  .poster {
    position: absolute;
    left: 230px; top: 47px;
    width: 740px; height: 1106px;
    background: var(--navy);
    color: var(--salmon);
  }
  .website {
    position: absolute; left: 60px; top: 42px;
    font-family: "Arimo", Arial, sans-serif;
    font-size: 17px; color: var(--rule);
    letter-spacing: 0.2px;
  }
  .lenses {
    position: absolute; left: 0; top: 0;
    width: 740px; height: 560px;
  }
  .rule {
    position: absolute; left: 60px; width: 615px; height: 4px;
    background: var(--rule);
  }
  .rule--top { top: 583px; }
  .rule--bottom { top: 909px; }
  .headline {
    position: absolute; left: 56px; top: 600px; width: 640px;
    font-family: "Abril Fatface", "Bodoni Moda", serif;
    font-weight: 400; font-size: 97px; line-height: 96px;
    text-transform: uppercase; white-space: nowrap;
    letter-spacing: 0.5px;
  }
  .brand {
    position: absolute; left: 56px; top: 950px;
    display: flex; align-items: center; gap: 12px;
    font-family: "Abril Fatface", "Bodoni Moda", serif;
    font-size: 32px; color: var(--salmon);
    letter-spacing: 1px; text-transform: uppercase;
  }
  .brand__mark {
    width: 38px; height: 38px; background: var(--salmon);
  }
  .contact {
    position: absolute; left: 393px; top: 960px;
    font-family: "Arimo", Arial, sans-serif;
  }
  .contact__phone {
    font-size: 23px; font-weight: 700; letter-spacing: 0.3px;
    margin-bottom: 6px;
  }
  .contact__address {
    font-size: 15.5px; line-height: 20px; width: 300px;
  }
</style>
</head>
<body>
  <main class="poster">
    <p class="website">www.brunor-agency.com</p>

    <svg class="lenses" viewBox="0 0 740 560" role="img"
         aria-label="Vue aérienne de Monaco au crépuscule, baie violette et immeubles illuminés, vue à travers des jumelles">
      <defs>
        <linearGradient id="dusk" x1="0" y1="0" x2="1" y2="1">
          <stop offset="0" stop-color="#b58ac6"/>
          <stop offset="0.35" stop-color="#9a6f9c"/>
          <stop offset="0.65" stop-color="#8a4f4a"/>
          <stop offset="1" stop-color="#2a1c1e"/>
        </linearGradient>
      </defs>
      <g class="lenses__frame" fill="none" stroke="var(--lens-edge)" stroke-width="9">
        <ellipse cx="198" cy="337" rx="180" ry="180"/>
        <ellipse cx="524" cy="337" rx="180" ry="180"/>
      </g>
      <g class="lenses__view" fill="url(#dusk)">
        <ellipse cx="198" cy="337" rx="180" ry="180"/>
        <ellipse cx="524" cy="337" rx="180" ry="180"/>
      </g>
    </svg>

    <div class="rule rule--top"></div>
    <h1 class="headline">Un nouveau<br>regard sur<br>l'immobilier</h1>
    <div class="rule rule--bottom"></div>

    <div class="brand">
      <span class="brand__mark"></span>
      <span class="brand__name">Brunor Agency</span>
    </div>

    <div class="contact">
      <p class="contact__phone">+377.93.48.25.71</p>
      <p class="contact__address">14 rue des Orvilles, Passage Marcellin, 98 000 Monaco</p>
    </div>
  </main>
</body>
</html>
```